RA Infrastructure Capability Statement

I need to design a two page Capability statement for our Civil Construction company that looks professional and can be issued to clients in electronic or print form to show our capabilities.

We have an existing Logo and website https://ra-infragroup.com.au/

It should include space for the below:
- Company heading/logo plus ABN, ACN and full contact details
- About Us – Mission, vision, values
- Our Service Offering / Core competencies
- Accreditations/certifications

Designs look the same

```html
<!DOCTYPE html>
<html lang="en">
<head>
<meta charset="utf-8">
<title>RA Infrastructure – Capability Statement</title>
<link href="https://fonts.googleapis.com/css2?family=Saira:wght@600;700&family=IBM+Plex+Sans:wght@400;600&family=Source+Sans+3:wght@300;400&family=Open+Sans:wght@400&display=swap" rel="stylesheet">
<style>
:root{
  --navy:#2e2f7f;
  --hero:#4e5098;
  --hero-deep:#3d3f88;
  --orange:#f6a81c;
  --ink:#3c3c48;
  --paper:#ffffff;
  --rule:#d6d7e6;
}
*{margin:0;padding:0;box-sizing:border-box}
html,body{width:900px;height:1200px;overflow:hidden;background:var(--paper)}
body{position:relative;font-family:"Source Sans 3",sans-serif;color:var(--ink)}
.page{position:absolute;width:372px;height:526px;background:var(--paper);box-shadow:0 0 6px rgba(0,0,0,.12);overflow:hidden}
.page--statement{left:49px;top:56px}
.page--services{left:484px;top:56px}
.page--logo-only{left:49px;top:610px}
.brand{position:absolute;left:26px;top:16px;display:flex;align-items:center;gap:5px}
.brand__mark{width:18px;height:18px;background:var(--orange)}
.brand__name{font-family:"Saira",sans-serif;font-weight:700;font-size:13px;color:var(--navy);letter-spacing:.2px}
.call{position:absolute;right:27px;top:13px;text-align:right;font-family:"IBM Plex Sans",sans-serif;font-size:6.2px;line-height:8.8px;color:var(--navy)}
.call b{font-weight:600}
.hero{position:absolute;left:0;top:48px;width:372px;height:124px;background:linear-gradient(120deg,#5a5c9f 0%,var(--hero) 45%,var(--hero-deep) 100%)}
.hero__title{position:absolute;left:26px;top:41px;font-family:"Saira",sans-serif;font-weight:700;font-size:25px;line-height:22px;color:#fff;letter-spacing:.3px}
.hero__contact{position:absolute;right:27px;text-align:right;font-family:"IBM Plex Sans",sans-serif;font-size:6.2px;line-height:8.8px;color:#fff}
.hero__contact b{font-weight:600}
.hero__contact .gap{display:block;height:4px}
.h-section{position:absolute;font-family:"Saira",sans-serif;font-weight:700;color:var(--navy);font-size:12.5px;line-height:13px;letter-spacing:.2px}
.copy{position:absolute;font-size:6.6px;line-height:8.3px;font-weight:300;color:var(--ink)}
.pillar{position:absolute;top:265px;width:100px}
.pillar h3{font-family:"Saira",sans-serif;font-weight:700;color:var(--navy);font-size:12.5px;line-height:13px;margin-bottom:4px}
.pillar p{font-size:6.6px;line-height:8.3px;font-weight:300}
.divider{position:absolute;top:266px;width:1px;height:72px;background:var(--rule)}
.competencies{position:absolute;left:27px;top:369px;list-style:none}
.competencies li{display:flex;align-items:center;height:16.7px;font-family:"Source Sans 3",sans-serif;font-size:8.6px;color:var(--ink)}
.competencies .tile{width:12px;height:12px;background:var(--orange);margin-right:9px}
.traits{position:absolute;top:439px;left:0;width:186px}
.trait{position:absolute;width:40px;text-align:center;font-size:5.9px;line-height:7.2px;color:#555}
.trait svg{display:block;margin:0 auto 3px}
.accred{position:absolute;left:186px;top:355px;width:160px;height:129px;border:1.3px solid var(--navy);border-radius:5px}
.accred__title{position:absolute;left:8px;top:-7px;width:144px;background:var(--paper);text-align:center;font-family:"Saira",sans-serif;font-weight:700;color:var(--navy);font-size:12.5px;line-height:15px}
.badge{position:absolute;top:37px;width:48px;height:48px;border-radius:50%;border:3px solid var(--navy);background:#eef0f8}
.footer{position:absolute;left:0;bottom:0;width:100%;height:30px;background:var(--navy);display:flex;align-items:center;justify-content:center;font-family:"IBM Plex Sans",sans-serif;font-weight:600;font-size:11px;color:var(--orange);letter-spacing:.3px}
.services-hero{position:absolute;left:0;top:48px;width:372px;height:134px;background:linear-gradient(110deg,#5b5da0 0%,var(--hero) 50%,#45478f 100%)}
.services-hero__title{position:absolute;right:240px;top:26px;text-align:right;font-family:"Saira",sans-serif;font-weight:700;color:#fff;font-size:15px;line-height:21.5px;letter-spacing:.8px}
.services-hero__rule{position:absolute;left:162px;top:25px;width:1.5px;height:88px;background:#fff}
.services-hero__intro{position:absolute;right:28px;top:14px;width:158px;text-align:right;font-family:"IBM Plex Sans",sans-serif;font-weight:600;font-size:5.9px;line-height:7.5px;color:#fff}
.service-bar{position:absolute;height:24px;background:var(--navy);color:#fff;font-family:"Saira",sans-serif;font-weight:600;font-size:13px;line-height:24px}
.photo{position:absolute;border-radius:6px;box-shadow:0 1px 4px rgba(0,0,0,.25)}
.photo--pipes{left:214px;top:198px;width:132px;height:131px;background:linear-gradient(160deg,#8a7a62 0%,#4a5aa0 45%,#b8ad9c 100%)}
.photo--excavation{left:25px;top:350px;width:132px;height:132px;background:linear-gradient(180deg,#eef0f0 0%,#cfd3d3 40%,#7d6a55 75%,#5a4a3a 100%)}
.note{position:absolute;left:440px;top:632px;font-family:"Open Sans",sans-serif;font-size:19px;color:#111;letter-spacing:-.2px}
</style>
</head>
<body>

<!-- Page one: capability statement with contact header -->
<section class="page page--statement">
  <div class="brand"><span class="brand__mark"></span><span class="brand__name">RA Infrastructure</span></div>
  <div class="call"><b>CALL US</b><br>Liam Carver 0400 555 101<br>Dean Whitfield 0400 555 202</div>
  <div class="hero" role="img" aria-label="Photo of hands over site plans with a hard hat and safety glasses, tinted blue">
    <h1 class="hero__title">CAPABILITIES<br>STATEMENT</h1>
    <div class="hero__contact" style="top:26px"><b>Find Us</b><br>12/40 Harbour Court,<br>Truganina VIC 3029<span class="gap"></span><b>E mail Us</b><br>tenders@ra-infragroup.com.au<span class="gap"></span><b>ABN 12 345 678 901</b><br><b>ACN 000 000 019</b></div>
  </div>
  <h2 class="h-section" style="left:27px;top:182px">ABOUT RA INFRASTRUCTURE</h2>
  <p class="copy" style="left:26px;top:200px;width:320px">RA Infrastructure is a specialist utilities contractor leveraging industry experience to provide exceptional outcomes. We are a client focused business that takes a ‘best-for-project’ approach in everything we do, and see honest, timely and transparent communication as one of our key strengths. Our business works in complex, high-risk environments and understands all safety, quality, and environmental considerations. We meticulously plan our projects with these key factors in mind, ensuring the requirements of the specific tasks are understood and well documented to satisfy our robust internal processes and rigorous external auditing.</p>
  <div class="pillar" style="left:27px"><h3>Our Mission</h3><p>Lorem ipsum dolor sit amet, consectetuer adipiscing elit, sed diam nonummy nibh euismod tincidunt ut laoreet dolore magna aliquam erat volutpat. Ut wisi enim ad minim veniam, quis nostrud</p></div>
  <span class="divider" style="left:126px"></span>
  <div class="pillar" style="left:137px"><h3>Our Vision</h3><p>Lorem ipsum dolor sit amet, consectetuer adipiscing elit, sed diam nonummy nibh euismod tincidunt ut laoreet dolore magna aliquam erat volutpat. Ut wisi enim ad minim veniam, quis nostrud</p></div>
  <span class="divider" style="left:237px"></span>
  <div class="pillar" style="left:249px"><h3>Our Values</h3><p>Lorem ipsum dolor sit amet, consectetuer adipiscing elit, sed diam nonummy nibh euismod tincidunt ut laoreet dolore magna aliquam erat volutpat. Ut wisi enim ad minim veniam, quis nostrud</p></div>
  <h2 class="h-section" style="left:27px;top:350px">CORE COMPETENCIES</h2>
  <ul class="competencies">
    <li><span class="tile"></span>Project / Program Management</li>
    <li><span class="tile"></span>Water Infrastructure</li>
    <li><span class="tile"></span>Gas Infrastructure</li>
    <li><span class="tile"></span>Civil Construction</li>
  </ul>
  <div class="traits">
    <div class="trait" style="left:28px"><svg width="26" height="26" viewBox="0 0 26 26"><circle cx="13" cy="13" r="13" fill="#2e2f7f"/><circle cx="13" cy="10" r="3.2" fill="#fff"/><path d="M7.5 19a5.5 5 0 0 1 11 0z" fill="#fff"/></svg>Trusted Professionals</div>
    <div class="trait" style="left:66px"><svg width="26" height="26" viewBox="0 0 26 26"><circle cx="13" cy="13" r="13" fill="#2e2f7f"/><path d="M13 6l6 2.5v4.5c0 3.5-2.6 5.8-6 7-3.4-1.2-6-3.5-6-7V8.5z" fill="#fff"/></svg>Safety Focused</div>
    <div class="trait" style="left:100px"><svg width="26" height="26" viewBox="0 0 26 26"><circle cx="13" cy="13" r="13" fill="#2e2f7f"/><path d="M8 13.5l3.3 3.3L18 10" fill="none" stroke="#fff" stroke-width="2.2" stroke-linecap="round" stroke-linejoin="round"/></svg>Quality Assurance</div>
    <div class="trait" style="left:135px"><svg width="26" height="26" viewBox="0 0 26 26"><circle cx="13" cy="13" r="13" fill="#2e2f7f"/><circle cx="10" cy="12" r="3" fill="#fff"/><circle cx="16" cy="12" r="3" fill="#fff"/><rect x="7" y="16" width="12" height="3" rx="1.5" fill="#fff"/></svg>Collaborative Problem Solvers</div>
  </div>
  <div class="accred">
    <h2 class="accred__title">ACCREDITATIONS<br>&amp;CERTIFICATIONS</h2>
    <span class="badge" style="left:21px" role="img" aria-label="Certification badge"></span>
    <span class="badge" style="left:87px" role="img" aria-label="Certification badge"></span>
  </div>
  <div class="footer">www.ra-infragroup.com.au</div>
</section>

<!-- Page two: service offering -->
<section class="page page--services">
  <div class="brand"><span class="brand__mark"></span><span class="brand__name">RA Infrastructure</span></div>
  <div class="call"><b>CALL US</b><br>Liam Carver 0400 555 101<br>Dean Whitfield 0400 555 202</div>
  <div class="services-hero" role="img" aria-label="Photo of a construction site with fencing, tinted blue">
    <h2 class="services-hero__title">OUR<br>SERVICE<br>OFFERING</h2>
    <span class="services-hero__rule"></span>
    <p class="services-hero__intro">RA Infrastructure prides itself on being a customer focused business, that takes the time to understand our clients’ key drivers and ensure we work collaboratively with them to achieve positive outcomes. We have a team of highly experienced project management professionals who are genuine, responsive, and transparent which enables us to make our client lives easier from the design phase to project completion. We have a self-perform field resource that carries enviable experience, which is supplemented by hand-picked sub-contractors that are known in the industry and are trusted partners.</p>
  </div>
  <div class="service-bar" style="left:0;top:197px;width:173px;padding-left:27px">Utilities</div>
  <p class="copy" style="left:25px;top:234px;width:150px">Our team has a wide-ranging utilities background which gives us a deep understanding of what is in the ground and the specific requirements for each individual asset. Through this experience we have developed relationships with asset owners and distributors to ensure we deliver projects that will stand the test of time and be valuable pieces of future networks. Our commitment to safety and quality has further strengthened these relationships and puts us in a position to be a trusted advisor when the inevitable challenges are faced.</p>
  <div class="photo photo--pipes" role="img" aria-label="Photo of blue water valves and copper pipes on gravel"></div>
  <div class="service-bar" style="left:196px;top:341px;width:176px;padding-left:37px">Civil Construction</div>
  <p class="copy" style="left:196px;top:381px;width:145px">Leveraging off our considerable utilities background, we have seen our civil construction offering continue to grow. We have a resource base of skilled operators who take immense pride in their work and enable us to deliver cost effective, efficient services. We maintain a ‘Tier 1’ mindset and hold ourselves to the highest standards, while still being an agile delivery partner that can be relied upon to deliver your next civil project.</p>
  <div class="photo photo--excavation" role="img" aria-label="Photo of an excavator digging a deep trench"></div>
  <div class="footer">www.ra-infragroup.com.au</div>
</section>

<!-- Page one alternative: logo only header -->
<section class="page page--logo-only">
  <div class="brand"><span class="brand__mark"></span><span class="brand__name">RA Infrastructure</span></div>
  <div class="hero" role="img" aria-label="Photo of hands over site plans with a hard hat and safety glasses, tinted blue">
    <h1 class="hero__title">CAPABILITIES<br>STATEMENT</h1>
    <div class="hero__contact" style="top:17px"><b>Find Us</b><br>12/40 Harbour Court,<br>Truganina VIC 3029<span class="gap"></span><b>Call Us</b><br>Liam Carver 0400 555 101<br>Dean Whitfield 0400 555 202<span class="gap"></span><b>E mail Us</b><br>tenders@ra-infragroup.com.au<span class="gap"></span><b>ABN 12 345 678 901</b><br><b>ACN 000 000 019</b></div>
  </div>
  <h2 class="h-section" style="left:27px;top:182px">ABOUT RA INFRASTRUCTURE</h2>
  <p class="copy" style="left:26px;top:200px;width:320px">RA Infrastructure is a specialist utilities contractor leveraging industry experience to provide exceptional outcomes. We are a client focused business that takes a ‘best-for-project’ approach in everything we do, and see honest, timely and transparent communication as one of our key strengths. Our business works in complex, high-risk environments and understands all safety, quality, and environmental considerations. We meticulously plan our projects with these key factors in mind, ensuring the requirements of the specific tasks are understood and well documented to satisfy our robust internal processes and rigorous external auditing.</p>
  <div class="pillar" style="left:27px"><h3>Our Mission</h3><p>Lorem ipsum dolor sit amet, consectetuer adipiscing elit, sed diam nonummy nibh euismod tincidunt ut laoreet dolore magna aliquam erat volutpat. Ut wisi enim ad minim veniam, quis nostrud</p></div>
  <span class="divider" style="left:126px"></span>
  <div class="pillar" style="left:137px"><h3>Our Vision</h3><p>Lorem ipsum dolor sit amet, consectetuer adipiscing elit, sed diam nonummy nibh euismod tincidunt ut laoreet dolore magna aliquam erat volutpat. Ut wisi enim ad minim veniam, quis nostrud</p></div>
  <span class="divider" style="left:237px"></span>
  <div class="pillar" style="left:249px"><h3>Our Values</h3><p>Lorem ipsum dolor sit amet, consectetuer adipiscing elit, sed diam nonummy nibh euismod tincidunt ut laoreet dolore magna aliquam erat volutpat. Ut wisi enim ad minim veniam, quis nostrud</p></div>
  <h2 class="h-section" style="left:27px;top:350px">CORE COMPETENCIES</h2>
  <ul class="competencies">
    <li><span class="tile"></span>Project / Program Management</li>
    <li><span class="tile"></span>Water Infrastructure</li>
    <li><span class="tile"></span>Gas Infrastructure</li>
    <li><span class="tile"></span>Civil Construction</li>
  </ul>
  <div class="traits">
    <div class="trait" style="left:28px"><svg width="26" height="26" viewBox="0 0 26 26"><circle cx="13" cy="13" r="13" fill="#2e2f7f"/><circle cx="13" cy="10" r="3.2" fill="#fff"/><path d="M7.5 19a5.5 5 0 0 1 11 0z" fill="#fff"/></svg>Trusted Professionals</div>
    <div class="trait" style="left:66px"><svg width="26" height="26" viewBox="0 0 26 26"><circle cx="13" cy="13" r="13" fill="#2e2f7f"/><path d="M13 6l6 2.5v4.5c0 3.5-2.6 5.8-6 7-3.4-1.2-6-3.5-6-7V8.5z" fill="#fff"/></svg>Safety Focused</div>
    <div class="trait" style="left:100px"><svg width="26" height="26" viewBox="0 0 26 26"><circle cx="13" cy="13" r="13" fill="#2e2f7f"/><path d="M8 13.5l3.3 3.3L18 10" fill="none" stroke="#fff" stroke-width="2.2" stroke-linecap="round" stroke-linejoin="round"/></svg>Quality Assurance</div>
    <div class="trait" style="left:135px"><svg width="26" height="26" viewBox="0 0 26 26"><circle cx="13" cy="13" r="13" fill="#2e2f7f"/><circle cx="10" cy="12" r="3" fill="#fff"/><circle cx="16" cy="12" r="3" fill="#fff"/><rect x="7" y="16" width="12" height="3" rx="1.5" fill="#fff"/></svg>Collaborative Problem Solvers</div>
  </div>
  <div class="accred">
    <h2 class="accred__title">ACCREDITATIONS<br>&amp;CERTIFICATIONS</h2>
    <span class="badge" style="left:21px" role="img" aria-label="Certification badge"></span>
    <span class="badge" style="left:87px" role="img" aria-label="Certification badge"></span>
  </div>
  <div class="footer">www.ra-infragroup.com.au</div>
</section>

<p class="note">LOGO ONLY HEADER</p>

</body>
</html>
```